Social Media Cover and Profile

We already have our own logo. We just need a fresh design on our social media pages. We are not happy with our current designs. We would like to incorporate our WHEE billboard and the colors are blue (#05143f) and white. You can also incorporate silver as well. We are a family law office (Divorce and Custody) We no longer want to incorporate the Beacon of Dunmore photo that we are currently using. You can look at our Facebook page; The Law Office of Miles T. Brandow.

Target Market(s)

Potential Clients

Industry/Entity Type

Family Law

Logo Text

Our Logo Is The Law Office of Miles T. Brandow with the Sheild

Requirements
Must have
• Text to include:
Central Pennslyvania's Premier Family Law Firm

Ability to be resized to and used as all images in social media, including but not limited to: Youtube Channel art, Facebook Cover and Profile.
Nice to have
• Darker color but we are open to "bright" ideas.

```html
<!DOCTYPE html>
<html lang="en">
<head>
<meta charset="utf-8">
<title>The Law Office of Miles T. Brandow – Cover</title>
<link href="https://fonts.googleapis.com/css2?family=Montserrat:wght@600&family=Sorts+Mill+Goudy&display=swap" rel="stylesheet">
<style>
  :root {
    --navy: #14213f;
    --brand-navy: #05143f;
    --silver-text: #8c8c8c;
    --frame-line: #a3a3a3;
    --ring-light: #f4f4f4;
    --ring-mid: #c9c9cc;
    --ring-dark: #9c9ca0;
    --paper: #ffffff;
  }
  html, body {
    margin: 0;
    padding: 0;
    width: 1200px;
    height: 455px;
    overflow: hidden;
    background: var(--paper);
  }
  .cover {
    position: relative;
    width: 1200px;
    height: 455px;
    background: var(--paper);
    overflow: hidden;
  }
  .frame {
    position: absolute;
    inset: 0;
  }
  .website {
    position: absolute;
    left: 26px;
    top: 20px;
    margin: 0;
    font-family: "Sorts Mill Goudy", Georgia, serif;
    font-size: 20px;
    color: #111;
    font-weight: 400;
    letter-spacing: 0.2px;
  }
  .firm-mark {
    position: absolute;
    left: 754px;
    top: 16px;
    display: flex;
    align-items: center;
    gap: 12px;
  }
  .firm-mark__square {
    width: 54px;
    height: 54px;
    background: var(--brand-navy);
  }
  .firm-mark__name {
    margin: 0;
    font-family: "Sorts Mill Goudy", Georgia, serif;
    font-weight: 400;
    font-size: 24px;
    line-height: 1.15;
    color: var(--brand-navy);
    text-transform: uppercase;
    letter-spacing: 0.5px;
  }
  .billboard {
    position: absolute;
    left: 0;
    top: 0;
    width: 1200px;
    height: 455px;
  }
  .ring {
    position: absolute;
    border-radius: 50% / 48%;
    background: linear-gradient(135deg, var(--ring-light) 0%, var(--ring-mid) 55%, var(--ring-dark) 100%);
  }
  .ring--band {
    left: 43px;
    top: 159px;
    width: 196px;
    height: 225px;
  }
  .ring--engagement {
    left: 258px;
    top: 87px;
    width: 176px;
    height: 297px;
    border-radius: 50% / 40%;
  }
  .ring-shadow {
    position: absolute;
    top: 378px;
    height: 16px;
    border-radius: 50%;
    background: radial-gradient(ellipse at center, rgba(0,0,0,0.22) 0%, rgba(0,0,0,0) 70%);
  }
  .ring-shadow--band { left: 50px; width: 190px; }
  .ring-shadow--engagement { left: 262px; width: 172px; }
  .ring-shadow--letters { left: 440px; width: 260px; }
  .billboard__word {
    position: absolute;
    left: 432px;
    top: 110px;
    margin: 0;
    font-family: "Montserrat", Arial, sans-serif;
    font-weight: 600;
    font-size: 292px;
    line-height: 1;
    color: var(--silver-text);
    letter-spacing: -6px;
  }
  .tagline {
    position: absolute;
    left: 0;
    right: 0;
    top: 414px;
    margin: 0;
    text-align: center;
    padding-left: 8px;
    font-family: "Sorts Mill Goudy", Georgia, serif;
    font-weight: 400;
    font-size: 29px;
    color: var(--navy);
    letter-spacing: 0.3px;
  }
</style>
</head>
<body>
  <main class="cover">
    <svg class="frame" width="1200" height="455" viewBox="0 0 1200 455" aria-hidden="true">
      <g stroke="var(--frame-line)" stroke-width="1.5" fill="none">
        <polyline points="732,14 14,14 14,432 245,432"/>
        <polyline points="964,432 1181,432 1181,88"/>
      </g>
    </svg>

    <p class="website">BrandowDivorce.com</p>

    <div class="firm-mark">
      <div class="firm-mark__square" aria-hidden="true"></div>
      <p class="firm-mark__name">The Law Office of<br>Miles T. Brandow</p>
    </div>

    <div class="billboard" aria-label="WHEE">
      <div class="ring-shadow ring-shadow--band"></div>
      <div class="ring-shadow ring-shadow--engagement"></div>
      <div class="ring-shadow ring-shadow--letters"></div>
      <div class="ring ring--band" role="img" aria-label="Silver wedding band standing upright, forming a letter"></div>
      <div class="ring ring--engagement" role="img" aria-label="Silver solitaire engagement ring standing upright, forming a letter"></div>
      <p class="billboard__word">EE</p>
    </div>

    <p class="tagline">Central Pennslyvania's Premier Family Law Firm</p>
  </main>
</body>
</html>
```